Business card for partnership

Plumbing and hvac company needing a minimal business card. We already have a logo i would like the front of the card just the logo and the back have all info.

Target Market(s)

Commercial facilities

Industry/Entity Type

Plumbing hvac

Contact Information for Business Card

We would like it double sided. Logo big and bold on the front and out info on the back. Our info on back would be name and position phone, email, and location

```html
<!DOCTYPE html>
<html lang="en">
<head>
<meta charset="utf-8">
<title>Ridgeway Mechanical – Business Card</title>
<link href="https://fonts.googleapis.com/css2?family=Lato:wght@400;700;900&display=swap" rel="stylesheet">
<style>
  :root {
    --backdrop: #1b1b1b;
    --card: #575757;
    --white: #ffffff;
    --soft-white: #e9e9e9;
    --orange: #f0842f;
  }
  * { box-sizing: border-box; margin: 0; padding: 0; }
  html, body {
    width: 1200px;
    height: 1122px;
    overflow: hidden;
    background: var(--backdrop);
    font-family: "Lato", sans-serif;
  }
  .card {
    position: absolute;
    width: 760px;
    height: 434px;
    background: var(--card);
    border-radius: 26px;
    box-shadow: 0 14px 40px rgba(0,0,0,0.55);
  }
  .card-front { left: 380px; top: 70px; display: flex; align-items: center; justify-content: center; gap: 22px; }
  .card-back { left: 60px; top: 600px; }

  .brand-mark {
    width: 34px;
    height: 34px;
    background: var(--orange);
    flex: none;
  }
  .brand-name {
    color: var(--white);
    font-weight: 900;
    font-size: 58px;
    letter-spacing: 2px;
    text-transform: uppercase;
    line-height: 1;
  }
  .back-brand {
    position: absolute;
    left: 46px;
    top: 44px;
    color: var(--orange);
    font-weight: 900;
    font-size: 30px;
    letter-spacing: 1px;
    text-transform: uppercase;
  }

  .contact-block {
    position: absolute;
    right: 46px;
    bottom: 40px;
    text-align: right;
  }
  .person-name {
    color: var(--white);
    font-weight: 700;
    font-size: 34px;
    letter-spacing: 1px;
    text-transform: uppercase;
    line-height: 1.1;
  }
  .person-role {
    color: var(--orange);
    font-size: 22px;
    margin-top: 2px;
  }
  .divider {
    width: 70px;
    height: 3px;
    background: var(--white);
    margin: 16px 0 14px auto;
  }
  .contact-list { list-style: none; }
  .contact-item {
    display: flex;
    align-items: center;
    justify-content: flex-end;
    gap: 14px;
    color: var(--soft-white);
    font-size: 19px;
    line-height: 1.55;
  }
  .contact-item.phone { font-weight: 700; font-size: 22px; color: var(--white); }
  .contact-icon { width: 16px; height: 16px; flex: none; fill: var(--orange); }
</style>
</head>
<body>
  <section class="card card-front" aria-label="Card front">
    <span class="brand-mark"></span>
    <span class="brand-name">Ridgeway Mechanical</span>
  </section>

  <section class="card card-back" aria-label="Card back">
    <div class="back-brand">Ridgeway</div>
    <div class="contact-block">
      <div class="person-name">Dale Morrow</div>
      <div class="person-role">Founder &amp; CEO</div>
      <div class="divider"></div>
      <ul class="contact-list">
        <li class="contact-item phone">(123) 456-7890
          <svg class="contact-icon" viewBox="0 0 24 24" aria-hidden="true"><path d="M6.6 10.8a15.1 15.1 0 0 0 6.6 6.6l2.2-2.2a1 1 0 0 1 1-.25 11.4 11.4 0 0 0 3.6.57 1 1 0 0 1 1 1V20a1 1 0 0 1-1 1A17 17 0 0 1 3 4a1 1 0 0 1 1-1h3.5a1 1 0 0 1 1 1c0 1.25.2 2.45.57 3.57a1 1 0 0 1-.25 1z"/></svg>
        </li>
        <li class="contact-item">info@ridgewaymech.com
          <svg class="contact-icon" viewBox="0 0 24 24" aria-hidden="true"><path d="M2 5h20v14H2z M4 7v.4l8 5 8-5V7l-8 5z" fill-rule="evenodd"/></svg>
        </li>
        <li class="contact-item">Your Address, City, State, Zip 1235
          <svg class="contact-icon" viewBox="0 0 24 24" aria-hidden="true"><path d="M12 2a7 7 0 0 0-7 7c0 5.2 7 13 7 13s7-7.8 7-13a7 7 0 0 0-7-7zm0 9.5A2.5 2.5 0 1 1 12 6.5a2.5 2.5 0 0 1 0 5z"/></svg>
        </li>
      </ul>
    </div>
  </section>
</body>
</html>
```